I need a mobile phone and tablet review site.

Hi everyone, I am looking for a professionally designed website which will review newly produced mobile phone and tablets. In the website users should be able to comment about newly produced phones. The website is to resemble gadget harbor. Which also review Mobile phones. There would be a category for tablets and a different category for mobile phone in the website. Under the Mobile category there should be a column for popular brands like Quelo, Dravenko and others. Same thing goes for the tablet category. My site should be eye catching.

```html
<!DOCTYPE html>
<html lang="en">
<head>
<meta charset="utf-8">
<title>Gadget Harbor — Phone &amp; Tablet Reviews</title>
<link href="https://fonts.googleapis.com/css2?family=Source+Sans+3:wght@300;400;600;700&display=swap" rel="stylesheet">
<style>
:root{
  --blue:#1fa8dc;
  --dark:#333333;
  --dark-2:#2b2b2b;
  --grey:#e4e4e4;
  --ink:#3a3a3a;
  --muted:#8a8a8a;
  --white:#ffffff;
  --night-top:#0e1520;
  --night-mid:#1b2634;
  --night-glow:#3a4a5c;
}
*{box-sizing:border-box;margin:0;padding:0}
html,body{width:1200px;height:3854px;overflow:hidden}
body{font-family:"Source Sans 3",Arial,sans-serif;color:var(--ink);background:var(--grey)}

/* header */
.site-header{height:90px;background:var(--blue);position:relative}
.logo{position:absolute;left:67px;top:28px;font-size:26px;font-weight:300;color:var(--white);letter-spacing:.5px}
.main-nav{position:absolute;left:591px;top:34px;display:flex}
.main-nav a{font-size:15px;font-weight:600;color:var(--white);text-decoration:none;margin-right:30px}
.main-nav a.is-active{color:var(--dark-2)}
.search{position:absolute;right:67px;top:34px;display:flex;align-items:center;gap:8px;color:var(--white);font-size:11px;opacity:.9}

/* photo fills (tones only) */
.thumb{display:block;width:241px;height:133px}
.thumb--watch{background:
  radial-gradient(ellipse 30% 60% at 62% 55%,#1d1d1f 0 55%,rgba(29,29,31,0) 75%),
  linear-gradient(100deg,#f4f4f4 0%,#e9e6df 40%,#b59a62 58%,#2a2a2c 72%,#f1f1f1 100%)}
.thumb--stage{background:
  radial-gradient(ellipse 40% 55% at 50% 60%,#c99c82 0 40%,rgba(201,156,130,0) 75%),
  linear-gradient(160deg,#18324f 0%,#24466b 45%,#5b6f86 75%,#c8ccd2 100%)}
.thumb--tablet{background:
  radial-gradient(ellipse 38% 45% at 48% 50%,#2d5fa8 0 50%,rgba(45,95,168,0) 80%),
  linear-gradient(135deg,#d8cfbf 0%,#e8e2d6 40%,#4a4a4c 75%,#2b2b2d 100%)}
.hero--phone{background:
  radial-gradient(ellipse 16% 46% at 52% 58%,#1b1f26 0 60%,rgba(27,31,38,0) 100%),
  radial-gradient(ellipse 22% 30% at 40% 78%,#d7a98b 0 45%,rgba(215,169,139,0) 100%),
  linear-gradient(110deg,#e8eef4 0%,#c9d5df 35%,#9fb3c4 55%,#dfe6ec 80%,#f3f5f7 100%)}

/* blocks */
.block{position:relative;overflow:hidden}
.block--popular{height:917px;background:linear-gradient(var(--dark) 0 167px,var(--grey) 167px)}
.block--latest{height:920px;background:var(--dark)}
.block--video{height:632px;background:var(--blue)}
.block__inner{position:absolute;left:67px;display:flex}
.block--popular .block__inner{top:57px}
.block--latest .block__inner{top:62px}
.block--video .block__inner{top:54px}
.block--video .rail{padding-top:14px}

.rail{width:241px}
.block-title{height:44px;position:relative;padding-top:8px;font-size:17px;font-weight:700;color:var(--white)}
.block-title::before{content:"";position:absolute;left:0;top:-4px;width:30px;height:3px;background:var(--blue)}
.block--video .block-title::before{background:var(--white)}

.rail-item{height:252px;position:relative;padding-top:13px}
.rail-item::before{content:"";position:absolute;left:0;top:0;width:30px;height:2px;background:var(--blue)}
.block--video .rail-item::before{background:var(--white)}
.rail-item p,.review-card p{margin-top:11px;font-size:14px;line-height:20px;color:var(--ink);padding-right:12px}
.block--latest .rail-item p{color:#e6e6e6}
.block--video .rail-item p{color:var(--white)}

.meta{display:flex;justify-content:space-between;align-items:center;margin-top:4px;font-size:10px;color:var(--muted)}
.meta span{display:flex;align-items:center;gap:5px}
.meta svg{width:12px;height:12px}
.block--video .meta{color:#dff3fb}

.divider{width:2px;margin-left:28px;height:800px}
.block--popular .divider{background:linear-gradient(#555 0 110px,#cfcfcf 110px)}
.block--latest .divider{background:#555}
.block--video .divider{background:#7fd0ee;height:520px}

.lead{width:766px;margin-left:28px}
.hero{width:766px;height:430px;position:relative}
.block--video .hero{height:362px}
.play{position:absolute;left:50%;top:50%;width:56px;height:56px;transform:translate(-50%,-50%)}
.lead h3{margin-top:12px;font-size:23px;line-height:29px;font-weight:400;color:var(--ink)}
.block--latest .lead h3{color:#eeeeee}
.block--video .lead h3{color:var(--white)}
.lead .meta{justify-content:flex-start;gap:26px;font-size:12px;margin-top:8px}
.lead .meta svg{width:15px;height:15px}

.gallery{display:flex;gap:23px;margin-top:22px}
.gallery figure{width:372px}
.gallery .thumb{width:372px;height:208px}
.gallery figcaption{margin-top:8px;font-size:10px;line-height:13px;color:var(--ink)}
.block--latest .gallery figcaption{color:#dddddd}
.gallery .meta{justify-content:flex-start;gap:16px;font-size:8px;margin-top:3px}
.gallery .meta svg{width:9px;height:9px}

/* reviews */
.block--reviews{height:648px;background:linear-gradient(var(--dark) 0 116px,var(--grey) 116px)}
.block--reviews .block-title{position:absolute;left:67px;top:69px}
.tabs{position:absolute;left:933px;top:69px;display:flex;gap:30px;font-size:17px;color:var(--white);padding-top:8px}
.tabs .tab{position:relative}
.tabs .tab.is-open::before{content:"";position:absolute;left:0;top:-12px;width:30px;height:3px;background:var(--blue)}
.dropdown{position:absolute;left:897px;top:98px;width:160px;background:var(--dark-2);z-index:2;list-style:none;font-size:10px;color:#ddd;text-align:center}
.dropdown li{height:18px;line-height:18px}
.dropdown li.is-current{background:var(--blue);color:var(--white)}
.review-grid{position:absolute;left:67px;top:113px;display:grid;grid-template-columns:repeat(4,241px);column-gap:34px}
.review-card{height:252px;position:relative}
.review-card::after{content:"";position:absolute;left:0;bottom:8px;width:30px;height:2px;background:var(--blue)}

/* about */
.block--about{height:647px;position:relative;color:var(--white);text-align:center}
.skyline{position:absolute;inset:0;background:
  radial-gradient(ellipse 70% 30% at 50% 92%,rgba(90,110,130,.55) 0%,rgba(90,110,130,0) 100%),
  radial-gradient(ellipse 8% 40% at 37% 70%,rgba(60,72,88,.6) 0%,rgba(60,72,88,0) 100%),
  linear-gradient(180deg,var(--night-top) 0%,var(--night-mid) 50%,var(--night-glow) 78%,#141b24 100%)}
.block--about .block-title{position:absolute;left:67px;top:69px;text-align:left}
.about-copy{position:absolute;left:270px;width:660px;top:245px}
.about-copy h2{font-size:26px;font-weight:400;letter-spacing:.5px}
.about-copy h4{font-size:15px;font-weight:400;margin-top:2px}
.about-copy p{font-size:12.5px;line-height:17px;margin-top:22px;color:#e6e6e6}
.about-copy a{display:inline-block;margin-top:36px;color:var(--blue);font-size:16px;text-decoration:none}
.copyright{position:absolute;left:0;right:0;bottom:30px;font-size:10px;color:#d0d0d0}
</style>
</head>
<body>

<svg width="0" height="0" style="position:absolute">
  <defs>
    <symbol id="i-clock" viewBox="0 0 16 16"><circle cx="8" cy="8" r="6.5" fill="none" stroke="currentColor" stroke-width="1.4"/><path d="M8 4v4l3 2" fill="none" stroke="currentColor" stroke-width="1.4"/></symbol>
    <symbol id="i-comment" viewBox="0 0 16 16"><path d="M2 3h9v6H6l-3 2.5V9H2z" fill="none" stroke="currentColor" stroke-width="1.3"/><path d="M12 6h2v5h-1v2l-2.5-2H7" fill="none" stroke="currentColor" stroke-width="1.3"/></symbol>
    <symbol id="i-play" viewBox="0 0 56 56"><circle cx="28" cy="28" r="26" fill="rgba(255,255,255,.35)" stroke="#fff" stroke-width="2"/><path d="M23 18l15 10-15 10z" fill="#fff"/></symbol>
  </defs>
</svg>

<header class="site-header">
  <div class="logo">YOURLOGO</div>
  <nav class="main-nav">
    <a class="is-active" href="#">Home</a><a href="#">Smartphones</a><a href="#">Tablets</a><a href="#">About</a><a href="#">Contact</a>
  </nav>
  <div class="search">Search
    <svg width="16" height="16" viewBox="0 0 16 16"><circle cx="6.5" cy="6.5" r="5" fill="none" stroke="#fff" stroke-width="2"/><path d="M10.5 10.5L15 15" stroke="#fff" stroke-width="2.2"/></svg>
  </div>
</header>

<section class="block block--popular">
  <div class="block__inner">
    <aside class="rail">
      <h2 class="block-title">Most Popular</h2>
      <article class="rail-item"><span class="thumb thumb--watch" role="img" aria-label="Smartwatch band close-up"></span><p>Neque non consectetuer ut nec vel porttitor eu tellus lacus amet vitae er, nearly every time</p><div class="meta"><span><svg><use href="#i-clock"/></svg>10h ago</span><span><svg><use href="#i-comment"/></svg>Comments</span></div></article>
      <article class="rail-item"><span class="thumb thumb--stage" role="img" aria-label="Presenter showing two smartphones"></span><p>Neque non consectetuer ut nec vel porttitor eu tellus lacus amet vitae er, nearly every time</p><div class="meta"><span><svg><use href="#i-clock"/></svg>10h ago</span><span><svg><use href="#i-comment"/></svg>Comments</span></div></article>
      <article class="rail-item"><span class="thumb thumb--tablet" role="img" aria-label="Tablet with tiled start screen"></span><p>Neque non consectetuer ut nec vel porttitor eu tellus lacus amet vitae er, nearly every time</p><div class="meta"><span><svg><use href="#i-clock"/></svg>9h ago</span><span><svg><use href="#i-comment"/></svg>Comments</span></div></article>
    </aside>
    <div class="divider"></div>
    <div class="lead">
      <div class="hero hero--phone" role="img" aria-label="Hand holding a smartphone in front of a city window"><svg class="play"><use href="#i-play"/></svg></div>
      <h3>Neque non consectetuer ut nec vel porttitor eu tellus lacus amet vitae er, nearly every time.</h3>
      <div class="meta"><span><svg><use href="#i-clock"/></svg>10h ago</span><span><svg><use href="#i-comment"/></svg>Comments</span></div>
      <div class="gallery">
        <figure><span class="thumb thumb--tablet" role="img" aria-label="Tablet with tiled start screen"></span><figcaption>Neque non consectetuer ut nec vel porttitor eu tellus lacus amet vitae er, nearly every time.</figcaption><div class="meta"><span><svg><use href="#i-clock"/></svg>9h ago</span><span><svg><use href="#i-comment"/></svg>Comments</span></div></figure>
        <figure><span class="thumb thumb--stage" role="img" aria-label="Presenter showing two smartphones"></span><figcaption>Neque non consectetuer ut nec vel porttitor eu tellus lacus amet vitae er, nearly every time.</figcaption><div class="meta"><span><svg><use href="#i-clock"/></svg>9h ago</span><span><svg><use href="#i-comment"/></svg>Comments</span></div></figure>
      </div>
    </div>
  </div>
</section>

<section class="block block--latest">
  <div class="block__inner">
    <aside class="rail">
      <h2 class="block-title">The Latest</h2>
      <article class="rail-item"><span class="thumb thumb--watch" role="img" aria-label="Smartwatch band close-up"></span><p>Neque non consectetuer ut nec vel porttitor eu tellus lacus amet vitae er, nearly every time</p><div class="meta"><span><svg><use href="#i-clock"/></svg>10h ago</span><span><svg><use href="#i-comment"/></svg>Comments</span></div></article>
      <article class="rail-item"><span class="thumb thumb--stage" role="img" aria-label="Presenter showing two smartphones"></span><p>Neque non consectetuer ut nec vel porttitor eu tellus lacus amet vitae er, nearly every time</p><div class="meta"><span><svg><use href="#i-clock"/></svg>10h ago</span><span><svg><use href="#i-comment"/></svg>Comments</span></div></article>
      <article class="rail-item"><span class="thumb thumb--tablet" role="img" aria-label="Tablet with tiled start screen"></span><p>Neque non consectetuer ut nec vel porttitor eu tellus lacus amet vitae er, nearly every time</p><div class="meta"><span><svg><use href="#i-clock"/></svg>9h ago</span><span><svg><use href="#i-comment"/></svg>Comments</span></div></article>
    </aside>
    <div class="divider"></div>
    <div class="lead">
      <div class="hero hero--phone" role="img" aria-label="Hand holding a smartphone in front of a city window"></div>
      <h3>Neque non consectetuer ut nec vel porttitor eu tellus lacus amet vitae er, nearly every time.</h3>
      <div class="meta"><span><svg><use href="#i-clock"/></svg>10h ago</span><span><svg><use href="#i-comment"/></svg>Comments</span></div>
      <div class="gallery">
        <figure><span class="thumb thumb--tablet" role="img" aria-label="Tablet with tiled start screen"></span><figcaption>Neque non consectetuer ut nec vel porttitor eu tellus lacus amet vitae er, nearly every time.</figcaption><div class="meta"><span><svg><use href="#i-clock"/></svg>9h ago</span><span><svg><use href="#i-comment"/></svg>Comments</span></div></figure>
        <figure><span class="thumb thumb--stage" role="img" aria-label="Presenter showing two smartphones"></span><figcaption>Neque non consectetuer ut nec vel porttitor eu tellus lacus amet vitae er, nearly every time.</figcaption><div class="meta"><span><svg><use href="#i-clock"/></svg>9h ago</span><span><svg><use href="#i-comment"/></svg>Comments</span></div></figure>
      </div>
    </div>
  </div>
</section>

<section class="block block--video">
  <div class="block__inner">
    <aside class="rail">
      <h2 class="block-title">Featured Video</h2>
      <article class="rail-item"><span class="thumb thumb--watch" role="img" aria-label="Smartwatch band close-up"></span><p>Neque non consectetuer ut nec vel porttitor eu tellus lacus amet vitae er, nearly every time</p><div class="meta"><span><svg><use href="#i-clock"/></svg>10h ago</span><span><svg><use href="#i-comment"/></svg>Comments</span></div></article>
      <article class="rail-item"><span class="thumb thumb--stage" role="img" aria-label="Presenter showing two smartphones"></span><p>Neque non consectetuer ut nec vel porttitor eu tellus lacus amet vitae er, nearly every time</p><div class="meta"><span><svg><use href="#i-clock"/></svg>10h ago</span><span><svg><use href="#i-comment"/></svg>Comments</span></div></article>
    </aside>
    <div class="divider"></div>
    <div class="lead">
      <div class="hero hero--phone" role="img" aria-label="Video still of a hand holding a smartphone"><svg class="play"><use href="#i-play"/></svg></div>
      <h3>Neque non consectetuer ut nec vel porttitor eu tellus lacus amet vitae er, nearly every time.</h3>
      <div class="meta"><span><svg><use href="#i-clock"/></svg>10h ago</span><span><svg><use href="#i-comment"/></svg>Comments</span></div>
    </div>
  </div>
</section>

<section class="block block--reviews">
  <h2 class="block-title">Product Reviews</h2>
  <div class="tabs"><span class="tab is-open">Smartphones</span><span class="tab">Tablets</span></div>
  <ul class="dropdown">
    <li class="is-current">Dravenko</li><li>Quelo Q</li><li>Lumen</li><li>Norvik</li><li>More brands listed...</li>
  </ul>
  <div class="review-grid">
    <article class="review-card"><span class="thumb thumb--watch" role="img" aria-label="Smartwatch band close-up"></span><p>Neque non consectetuer ut nec vel porttitor eu tellus lacus amet vitae er, nearly every time</p><div class="meta"><span><svg><use href="#i-clock"/></svg>10h ago</span><span><svg><use href="#i-comment"/></svg>Comments</span></div></article>
    <article class="review-card"><span class="thumb thumb--watch" role="img" aria-label="Smartwatch band close-up"></span><p>Neque non consectetuer ut nec vel porttitor eu tellus lacus amet vitae er, nearly every time</p><div class="meta"><span><svg><use href="#i-clock"/></svg>10h ago</span><span><svg><use href="#i-comment"/></svg>Comments</span></div></article>
    <article class="review-card"><span class="thumb thumb--watch" role="img" aria-label="Smartwatch band close-up"></span><p>Neque non consectetuer ut nec vel porttitor eu tellus lacus amet vitae er, nearly every time</p><div class="meta"><span><svg><use href="#i-clock"/></svg>10h ago</span><span><svg><use href="#i-comment"/></svg>Comments</span></div></article>
    <article class="review-card"><span class="thumb thumb--watch" role="img" aria-label="Smartwatch band close-up"></span><p>Neque non consectetuer ut nec vel porttitor eu tellus lacus amet vitae er, nearly every time</p><div class="meta"><span><svg><use href="#i-clock"/></svg>10h ago</span><span><svg><use href="#i-comment"/></svg>Comments</span></div></article>
    <article class="review-card"><span class="thumb thumb--watch" role="img" aria-label="Smartwatch band close-up"></span><p>Neque non consectetuer ut nec vel porttitor eu tellus lacus amet vitae er, nearly every time</p><div class="meta"><span><svg><use href="#i-clock"/></svg>10h ago</span><span><svg><use href="#i-comment"/></svg>Comments</span></div></article>
    <article class="review-card"><span class="thumb thumb--watch" role="img" aria-label="Smartwatch band close-up"></span><p>Neque non consectetuer ut nec vel porttitor eu tellus lacus amet vitae er, nearly every time</p><div class="meta"><span><svg><use href="#i-clock"/></svg>10h ago</span><span><svg><use href="#i-comment"/></svg>Comments</span></div></article>
    <article class="review-card"><span class="thumb thumb--watch" role="img" aria-label="Smartwatch band close-up"></span><p>Neque non consectetuer ut nec vel porttitor eu tellus lacus amet vitae er, nearly every time</p><div class="meta"><span><svg><use href="#i-clock"/></svg>10h ago</span><span><svg><use href="#i-comment"/></svg>Comments</span></div></article>
    <article class="review-card"><span class="thumb thumb--watch" role="img" aria-label="Smartwatch band close-up"></span><p>Neque non consectetuer ut nec vel porttitor eu tellus lacus amet vitae er, nearly every time</p><div class="meta"><span><svg><use href="#i-clock"/></svg>10h ago</span><span><svg><use href="#i-comment"/></svg>Comments</span></div></article>
  </div>
</section>

<section class="block block--about">
  <div class="skyline" role="img" aria-label="City skyline at night with an observation tower"></div>
  <h2 class="block-title">Who We Are</h2>
  <div class="about-copy">
    <h2>TEXT HERE SOMETHING LIKE A TITLE</h2>
    <h4>THIS IS PARALLAX EFFECT</h4>
    <p>Lorem ipsum dolor sit amet, ut purus, mauris amet. Amet eu, bibendum molestie massa fusce rutrum justo, bibendum tincidunt risus eu nulla porta, fringilla nibh ultricies ut, id vel ac tincidunt risus sed. Urna sed sapien, in nulla porttitor ipsum duis, tempus cras ullamcorper, porta eget, in a volutpat molestie vitae metus consequat. Parturient nunc tellus rutrum placerat diam ipsum, rhoncus faucibus nulla tristique feugiat.</p>
    <a href="#">CONTACT US</a>
  </div>
  <div class="copyright">© COPYRIGHT 2016. YOUR BUSINESS NAME. ALL RIGHTS RESERVED.</div>
</section>

</body>
</html>
```